Pelican Shoals Postcard Design

I am a real estate agent
I am marketing a gulf access waterfront community is southwest florida. I would like to do Just Listed and Just Sold post cards

So this will be two different post cards

In addition to the pictures I have uploaded mock ups of an idea of what I would like for the front and the back

I would like this done glossy on both sides

```html
<!DOCTYPE html>
<html lang="en">
<head>
<meta charset="utf-8">
<title>Pelican Shoals Postcards</title>
<link rel="stylesheet" href="https://fonts.googleapis.com/css2?family=Arimo:wght@400;700&family=Libre+Baskerville:wght@700&family=Yellowtail&family=Varela+Round&display=swap">
<style>
  :root {
    --green: #2f8f46;
    --green-dark: #1f6e33;
    --blue: #1f5ea8;
    --blue-dark: #163f7a;
    --ink: #1a1a1a;
    --paper: #ffffff;
    --page: #ffffff;
    --frame: #222222;
  }
  * { box-sizing: border-box; margin: 0; padding: 0; }
  html, body { width: 1200px; height: 919px; overflow: hidden; background: var(--page); }
  .sheet { position: relative; width: 1200px; height: 919px; }

  .card { position: absolute; width: 580px; height: 447px; border: 1.5px solid var(--frame); overflow: hidden; }
  .card--front-sold { left: 7px; top: 9px; }
  .card--back-sold { left: 611px; top: 9px; background: var(--paper); }
  .card--front-listed { left: 7px; top: 465px; }
  .card--back-listed { left: 611px; top: 465px; background: var(--paper); }

  .scene { position: absolute; inset: 0; }
  .scene--canal {
    background: linear-gradient(180deg, #86aee0 0%, #a9c6ea 28%, #4f7a3c 36%, #3c6631 52%, #6f8fa8 58%, #3f5f78 78%, #2d475c 100%);
  }
  .scene--aerial {
    background: linear-gradient(180deg, #4f79bd 0%, #8fb0d8 24%, #8aa0a8 34%, #7c8f7c 55%, #6b7d5f 78%, #4d6a40 100%);
  }

  .state-badge { position: absolute; left: 22px; top: 21px; width: 112px; height: 112px; }
  .state-badge__ring { position: absolute; left: 8px; top: 4px; width: 108px; height: 108px; border-radius: 50%; }
  .state-badge__disc { position: absolute; left: 0; top: 0; width: 106px; height: 106px; border-radius: 50%; background: var(--paper); padding: 10px; }
  .state-badge__map { width: 100%; height: 100%; border-radius: 50%; background: radial-gradient(circle at 55% 45%, #3c9a4a 0%, #5cae5e 45%, #e9f2e6 75%); }

  .ribbon { position: absolute; left: 162px; width: 256px; height: 72px; }
  .card--front-sold .ribbon { top: 37px; }
  .card--front-listed .ribbon { top: 52px; }
  .ribbon svg { position: absolute; inset: 0; }
  .ribbon__label { position: absolute; inset: 0; display: flex; align-items: center; justify-content: center;
    font-family: "Libre Baskerville", serif; font-weight: 700; font-size: 31px; color: var(--paper); letter-spacing: 0.5px; }

  .place-name { position: absolute; left: 0; width: 580px; text-align: center;
    font-family: "Yellowtail", cursive; font-size: 54px; color: var(--paper); }
  .card--front-sold .place-name { top: 112px; left: -12px; text-shadow: 3px 3px 0 var(--green-dark), -1px -1px 0 var(--green-dark); }
  .card--front-listed .place-name { top: 208px; left: -10px; text-shadow: 3px 3px 0 var(--blue-dark), -1px -1px 0 var(--blue-dark); }

  .inset { position: absolute; width: 124px; height: 124px; }
  .card--front-sold .inset { left: 430px; top: 25px; }
  .card--front-listed .inset { left: 436px; top: 34px; }
  .inset__ring { position: absolute; left: 10px; top: 0; width: 124px; height: 124px; border-radius: 50%; }
  .inset__photo { position: absolute; left: 0; top: 2px; width: 120px; height: 120px; border-radius: 50%; border: 3px solid var(--paper); }
  .inset__photo--aerial { background: linear-gradient(180deg, #6e94c9 0%, #8aa6b6 30%, #7b8c6d 60%, #5b7048 100%); }
  .inset__photo--canal { background: linear-gradient(180deg, #8fb4e4 0%, #4c7a3c 40%, #5b7f98 60%, #2f4b62 100%); }

  .agent-tag { position: absolute; left: 332px; width: 236px; height: 58px; border-radius: 12px;
    display: flex; align-items: center; gap: 10px; padding: 0 10px;
    font-family: "Varela Round", sans-serif; color: var(--paper); font-size: 17px; line-height: 22px; }
  .card--front-sold .agent-tag { top: 375px; background: var(--green); }
  .card--front-listed .agent-tag { top: 330px; left: 333px; background: var(--blue); }
  .agent-tag__mark { width: 26px; height: 26px; flex: none; background: var(--paper); border-radius: 3px; }

  .sender { position: absolute; left: 15px; top: 28px; display: flex; gap: 10px; font-family: "Arimo", sans-serif; color: var(--ink); }
  .sender__mark { width: 42px; height: 42px; margin-top: 6px; background: var(--ink); border-radius: 4px; flex: none; }
  .sender__name { font-size: 21px; line-height: 24px; }
  .sender__line { font-size: 11.5px; line-height: 15px; font-weight: 700; }

  .notice { position: absolute; left: 55px; top: 162px; font-family: "Arimo", sans-serif; font-weight: 700; font-size: 18.5px; color: var(--ink); }
  .price-line { position: absolute; left: 55px; top: 212px; display: flex; align-items: flex-end;
    font-family: "Arimo", sans-serif; font-weight: 700; font-size: 18.5px; color: var(--ink); }
  .blank { display: inline-block; border-bottom: 1.5px solid var(--ink); height: 18px; }
  .blank--price { width: 224px; margin: 0 12px 2px 14px; }
  .blank--date { width: 156px; margin: 0 0 2px 12px; }

  .invite { position: absolute; left: 16px; top: 289px; width: 250px; font-family: "Arimo", sans-serif; font-weight: 700; font-size: 14.5px; line-height: 17.5px; color: var(--ink); }
  .recipient { position: absolute; left: 306px; top: 294px; font-family: "Arimo", sans-serif; font-weight: 700; font-size: 14.5px; color: var(--ink); }
  .contact { position: absolute; left: 16px; top: 374px; font-family: "Arimo", sans-serif; font-weight: 700; font-size: 14.5px; line-height: 19px; color: var(--ink); }
</style>
</head>
<body>
<main class="sheet">

  <!-- Just Sold front -->
  <section class="card card--front-sold">
    <div class="scene scene--canal" role="img" aria-label="Photo of a fishing boat cruising down a palm-lined canal past waterfront homes"></div>
    <div class="state-badge">
      <div class="state-badge__ring" style="background: var(--green);"></div>
      <div class="state-badge__disc"><div class="state-badge__map" role="img" aria-label="Map of Florida marking the community location"></div></div>
    </div>
    <div class="ribbon">
      <svg viewBox="0 0 256 72" width="256" height="72"><path d="M0,4 Q128,20 256,4 L238,36 L256,68 Q128,52 0,68 L18,36 Z" fill="var(--green)"/></svg>
      <span class="ribbon__label">Just Sold</span>
    </div>
    <h2 class="place-name">Pelican Shoals</h2>
    <div class="inset">
      <div class="inset__ring" style="background: var(--green);"></div>
      <div class="inset__photo inset__photo--aerial" role="img" aria-label="Aerial photo of the waterfront community"></div>
    </div>
    <div class="agent-tag"><span class="agent-tag__mark"></span><span>harbor-tern realty<br>Marina Kessler Broker</span></div>
  </section>

  <!-- Just Sold back -->
  <section class="card card--back-sold">
    <div class="sender">
      <span class="sender__mark"></span>
      <div>
        <p class="sender__name">Marina Kessler</p>
        <p class="sender__line">Harbor Tern Realty</p>
        <p class="sender__line">PO Box 418</p>
        <p class="sender__line">Palm Inlet, FL 33990</p>
      </div>
    </div>
    <p class="notice">on your block of Pelican Shoals has just sold</p>
    <p class="price-line">at $<span class="blank blank--price"></span>on<span class="blank blank--date"></span></p>
    <p class="invite">Please contact me if you are interested in buying or selling property in the area.</p>
    <p class="recipient">To:</p>
    <p class="contact">941-555-0147<br>marina.kessler@example.com</p>
  </section>

  <!-- Just Listed front -->
  <section class="card card--front-listed">
    <div class="scene scene--aerial" role="img" aria-label="Aerial photo of the canal community stretching to the gulf"></div>
    <div class="state-badge">
      <div class="state-badge__ring" style="background: var(--blue);"></div>
      <div class="state-badge__disc"><div class="state-badge__map" role="img" aria-label="Map of Florida marking the community location"></div></div>
    </div>
    <div class="ribbon">
      <svg viewBox="0 0 256 72" width="256" height="72"><path d="M0,4 Q128,20 256,4 L238,36 L256,68 Q128,52 0,68 L18,36 Z" fill="var(--blue)"/></svg>
      <span class="ribbon__label">Just Listed</span>
    </div>
    <h2 class="place-name">Pelican Shoals</h2>
    <div class="inset">
      <div class="inset__ring" style="background: var(--blue);"></div>
      <div class="inset__photo inset__photo--canal" role="img" aria-label="Photo of a boat on a palm-lined canal"></div>
    </div>
    <div class="agent-tag"><span class="agent-tag__mark"></span><span>harbor-tern realty<br>Marina Kessler Broker</span></div>
  </section>

  <!-- Just Listed back -->
  <section class="card card--back-listed">
    <div class="sender">
      <span class="sender__mark"></span>
      <div>
        <p class="sender__name">Marina Kessler</p>
        <p class="sender__line">Harbor Tern Realty</p>
        <p class="sender__line">PO Box 418</p>
        <p class="sender__line">Palm Inlet, FL 33990</p>
      </div>
    </div>
    <p class="notice">on your block of Pelican Shoals has just listed</p>
    <p class="price-line">at $<span class="blank blank--price"></span>on<span class="blank blank--date"></span></p>
    <p class="invite">Please contact me if you are interested in buying or selling property in the area.</p>
    <p class="recipient">To:</p>
    <p class="contact">941-555-0147<br>marina.kessler@example.com</p>
  </section>

</main>
</body>
</html>
```